Parcel Haven
Website design - Gifts and Occasions
Website design
Gifts and Occasions
The company is a gift giving service that helps people pick out the perfect gift based on an algorthim
above header
https://www.pallorby.net/
BrightMarkup BrightMarkup

```html
<!DOCTYPE html>
<html lang="en">
<head>
<meta charset="utf-8">
<title>Parcel Haven — Sign Up</title>
<link rel="stylesheet" href="https://fonts.googleapis.com/css2?family=Roboto:wght@400;500&family=Open+Sans:wght@400&display=swap">
<style>
  :root {
    --brown: #7a4b0c;
    --brown-text: #8a5a16;
    --teal: #5fb3c0;
    --teal-line: #b9dfe4;
    --page: #f4f9fa;
    --white: #ffffff;
    --field-border: #c9e3e7;
    --text: #3d3d3d;
    --label: #555555;
    --placeholder: #6d6d6d;
  }
  * { box-sizing: border-box; margin: 0; padding: 0; }
  html, body { width: 1200px; height: 787px; overflow: hidden; background: var(--white); }
  body { font-family: "Roboto", Arial, sans-serif; color: var(--text); position: relative; }

  .site-header {
    position: absolute; left: 0; top: 0; width: 1200px; height: 111px;
    background: var(--white); border-bottom: 2px solid var(--teal-line);
  }
  .brand {
    position: absolute; left: 144px; top: 14px; width: 92px; height: 86px;
    display: flex; flex-direction: column; align-items: center; gap: 6px;
  }
  .brand-mark { width: 58px; height: 46px; background: var(--teal-line); }
  .brand-name { font-size: 14px; color: var(--teal); font-weight: 400; white-space: nowrap; }

  .login { position: absolute; left: 598px; top: 22px; }
  .login-field { position: absolute; top: 0; }
  .login-field label { display: block; font-size: 14px; color: var(--label); height: 19px; }
  .login-field .input { width: 186px; height: 38px; background: var(--white); border: 1px solid var(--field-border); }
  .login-user { left: 0; }
  .login-pass { left: 196px; }
  .btn {
    position: absolute; background: var(--brown); color: var(--white);
    font-family: "Roboto", Arial, sans-serif; font-weight: 500; border: none;
    display: flex; align-items: center; justify-content: center;
  }
  .btn-login { left: 391px; top: 19px; width: 70px; height: 38px; font-size: 16px; }

  .main { position: absolute; left: 0; top: 111px; width: 1200px; height: 595px; background: var(--page); }

  .about { position: absolute; left: 142px; top: 58px; width: 410px; }
  .about h2 { font-weight: 500; font-size: 32px; color: var(--brown-text); margin-bottom: 6px; }
  .about p { font-family: "Open Sans", Arial, sans-serif; font-size: 14.5px; line-height: 30px; color: var(--text); margin-bottom: 28px; }

  .signup { position: absolute; left: 598px; top: 33px; width: 460px; height: 560px; }
  .signup h1 { font-weight: 400; font-size: 37px; color: var(--brown-text); height: 62px; }
  .field {
    position: absolute; height: 37px; background: var(--white); border: 1px solid var(--field-border);
    font-size: 15px; color: var(--placeholder); padding-left: 10px; display: flex; align-items: center;
  }
  .field .caret { position: absolute; right: 10px; top: 14px; }
  .section-label { position: absolute; left: 0; font-size: 17px; line-height: 20px; color: var(--label); }
  .radio-row { position: absolute; left: 0; top: 367px; display: flex; align-items: center; font-size: 15px; line-height: 18px; color: var(--label); }
  .radio { width: 16px; height: 16px; border: 1px solid #9aa; border-radius: 50%; background: var(--white); margin-right: 10px; }
  .radio-row span.gap { width: 30px; }
  .btn-signup { left: 0; top: 487px; width: 112px; height: 36px; font-size: 20px; }

  .site-footer { position: absolute; left: 142px; top: 716px; font-size: 14px; color: var(--teal); line-height: 29px; }
</style>
</head>
<body>
  <header class="site-header">
    <div class="brand">
      <div class="brand-mark"></div>
      <div class="brand-name">Parcel Haven</div>
    </div>
    <div class="login">
      <div class="login-field login-user"><label>User Name</label><div class="input"></div></div>
      <div class="login-field login-pass"><label>Password</label><div class="input"></div></div>
      <div class="btn btn-login">Log in</div>
    </div>
  </header>

  <main class="main">
    <section class="about">
      <h2>About Us</h2>
      <p>Parcel Haven is a gift giving service that recommends the best gift for your personal or professional relationship. We will organize your upcoming events and notify you if a gift may need to be sent.</p>
      <p>Parcel Haven utilizes complex computer algorithms to recommend you a gift.</p>
    </section>

    <section class="signup">
      <h1>Sign Up</h1>
      <div class="field" style="left:0;top:62px;width:225px;">First Name</div>
      <div class="field" style="left:235px;top:62px;width:225px;">Last Name</div>
      <div class="field" style="left:0;top:108px;width:460px;">Email</div>
      <div class="field" style="left:0;top:153px;width:460px;">User Name</div>
      <div class="field" style="left:0;top:199px;width:225px;">Password</div>
      <div class="field" style="left:235px;top:199px;width:225px;">Re-enter Password</div>
      <div class="field" style="left:0;top:244px;width:460px;">Security Question
        <svg class="caret" width="14" height="8" viewBox="0 0 14 8"><path d="M0 0H14L7 8Z" fill="#5fb3c0"/></svg></div>
      <div class="field" style="left:0;top:290px;width:460px;">Answer</div>

      <div class="section-label" style="top:343px;">Gender</div>
      <div class="radio-row">
        <span class="radio"></span>Male<span class="gap"></span><span class="radio"></span>Female
      </div>
      <div class="section-label" style="top:396px;">Birthday</div>
      <div class="field" style="left:0;top:422px;width:146px;">Month
        <svg class="caret" width="14" height="8" viewBox="0 0 14 8"><path d="M0 0H14L7 8Z" fill="#5fb3c0"/></svg></div>
      <div class="field" style="left:156px;top:422px;width:148px;">Day
        <svg class="caret" width="14" height="8" viewBox="0 0 14 8"><path d="M0 0H14L7 8Z" fill="#5fb3c0"/></svg></div>
      <div class="field" style="left:312px;top:422px;width:148px;">Year
        <svg class="caret" width="14" height="8" viewBox="0 0 14 8"><path d="M0 0H14L7 8Z" fill="#5fb3c0"/></svg></div>

      <div class="btn btn-signup">SIGN UP</div>
    </section>
  </main>

  <footer class="site-footer">
    <div>Parcel Haven © 2014</div>
    <div>English (US)</div>
  </footer>
</body>
</html>
```